Bramwell Ridge Minerals

Looking for a cool, glossy business card...white with our logo on one side and then the a smaller version of the logo on the other side (top left hand corner) and then the name and position of the person next to it, and then the office address and email address on the bottom left hand corner and the phone numbers & email address on the bottom right hand corner. I have the logo already...can pass it on when you're ready.

```html
<!DOCTYPE html>
<html lang="en">
<head>
<meta charset="utf-8">
<title>Bramwell Ridge Minerals — Business Card</title>
<link rel="stylesheet" href="https://fonts.googleapis.com/css2?family=Crimson+Text:wght@400;600&display=swap">
<style>
  :root {
    --backdrop: #c9c9c9;
    --card-red: #a10020;
    --card-red-deep: #8e0016;
    --card-red-light: #b3102e;
    --edge-blue: #1a1aa6;
    --name-blue: #2b2bd0;
    --ink-white: #f4f1f1;
    --card-white: #f3f2f2;
    --card-white-shade: #e2e0e0;
    --logo-ink: #2a2a2e;
    --accent-blue: #1f2fb8;
    --text-font: "Crimson Text", Georgia, serif;
  }
  * { box-sizing: border-box; margin: 0; padding: 0; }
  html, body {
    width: 1200px; height: 800px; overflow: hidden;
    background: var(--backdrop);
    font-family: var(--text-font);
  }
  .canvas { position: relative; width: 1200px; height: 800px; }

  .card {
    position: absolute;
    width: 600px; height: 340px;
    border-radius: 3px;
    box-shadow: 0 14px 30px rgba(0,0,0,0.25);
  }

  /* Back side */
  .card--back {
    left: 70px; top: 90px;
    background: linear-gradient(120deg, var(--card-red-light) 0%, var(--card-red) 45%, var(--card-red-deep) 100%);
    border-bottom: 6px solid var(--edge-blue);
    color: var(--ink-white);
    z-index: 2;
  }
  .back-logo {
    position: absolute; left: 40px; top: 60px;
    display: flex; align-items: center; gap: 8px;
    font-size: 15px; font-weight: 600; color: var(--ink-white);
    letter-spacing: 0.5px;
  }
  .back-logo .mark {
    width: 12px; height: 12px; background: var(--ink-white);
  }
  .divider {
    position: absolute; left: 250px; top: 40px;
    width: 1px; height: 90px;
    background: linear-gradient(to bottom, transparent, rgba(255,255,255,0.7), transparent);
  }
  .person { position: absolute; left: 272px; top: 48px; }
  .person-name { font-size: 30px; color: var(--name-blue); line-height: 1.05; }
  .person-role { font-size: 17px; color: var(--ink-white); }

  .contact { position: absolute; font-size: 16px; line-height: 1.35; }
  .contact-row { display: flex; align-items: flex-start; gap: 8px; }
  .contact-row svg { flex: none; margin-top: 3px; }
  .contact--office { left: 36px; bottom: 28px; }
  .contact--direct { right: 30px; bottom: 28px; text-align: right; }
  .contact--direct .contact-row { justify-content: flex-end; }

  /* Front side */
  .card--front {
    left: 530px; top: 390px;
    background: linear-gradient(110deg, var(--card-white-shade) 0%, var(--card-white) 55%, #ffffff 80%, var(--card-white-shade) 100%);
    z-index: 1;
  }
  .front-logo {
    position: absolute; left: 0; right: 0; top: 0; bottom: 0;
    display: flex; align-items: center; justify-content: center; gap: 12px;
    font-size: 34px; font-weight: 600; color: var(--logo-ink);
    letter-spacing: 1px;
  }
  .front-logo .mark {
    width: 16px; height: 16px; border-radius: 50%; background: var(--accent-blue);
  }
</style>
</head>
<body>
<main class="canvas">

  <section class="card card--back" aria-label="Business card back">
    <div class="back-logo"><span class="mark"></span><span>Bramwell Ridge Minerals</span></div>
    <div class="divider"></div>
    <div class="person">
      <div class="person-name">Daniel Harrow</div>
      <div class="person-role">President</div>
    </div>

    <div class="contact contact--office">
      <div class="contact-row">
        <svg width="11" height="14" viewBox="0 0 11 14" aria-hidden="true"><path d="M5.5 0C2.5 0 0 2.4 0 5.3 0 9 5.5 14 5.5 14S11 9 11 5.3C11 2.4 8.5 0 5.5 0Zm0 7.4a2 2 0 1 1 0-4 2 2 0 0 1 0 4Z" fill="var(--edge-blue)"/></svg>
        <div>4120 Larkspur Way<br>Fairbanks, Alaska 99712</div>
      </div>
      <div class="contact-row">
        <svg width="13" height="10" viewBox="0 0 13 10" aria-hidden="true"><rect width="13" height="10" rx="1" fill="var(--edge-blue)"/><path d="M1 1.5l5.5 4 5.5-4" stroke="#fff" stroke-width="1" fill="none"/></svg>
        <div>dharrow@bramwellridgeminerals.com</div>
      </div>
    </div>

    <div class="contact contact--direct">
      <div class="contact-row">
        <div>555-014-2287</div>
        <svg width="12" height="12" viewBox="0 0 12 12" aria-hidden="true"><path d="M2.4 0.6 4.3 2.5 3.3 4.2c.7 1.6 2 2.9 3.6 3.6l1.6-1 2 1.9-1.3 2.4C4.6 10.9 1 7.2.2 1.9Z" fill="var(--edge-blue)"/></svg>
      </div>
      <div class="contact-row">
        <div>info@bramwellridge.com</div>
        <svg width="13" height="10" viewBox="0 0 13 10" aria-hidden="true"><rect width="13" height="10" rx="1" fill="var(--edge-blue)"/><path d="M1 1.5l5.5 4 5.5-4" stroke="#fff" stroke-width="1" fill="none"/></svg>
      </div>
    </div>
  </section>

  <section class="card card--front" aria-label="Business card front">
    <div class="front-logo"><span class="mark"></span><span>Bramwell Ridge Minerals</span></div>
  </section>

</main>
</body>
</html>
```